Quimby's Yard & Garden Center Business Card Update

I need an updated Business card design for my Lawn and Garden Center. We do Landscaping installs, Lawn Mowing, Snow Removal and also have a Garden Center Retail Division. I uploaded a few of our previous business cards to give an idea of what we are starting with. The main goal of this update is to simplify and modernize the business card, not all of the services that are on the previous cards has to be on the new one but I would still like to highlight our main services. There is also a sample of our logo that Can be used in the design.

Industry/Entity Type

Landscaping

Contact Information for Business Card

Morris Quimby
Morris@Quimbysyardandgarden.example
Business (555) 201-7784
Cell (555) 318-6092

Colors

Designer to choose colors to be used in the design.

Requirements
Must have
• Services Provided :
• Landscaping
• Lawn Maintenance
• Snow Removal
• Garden Center

```html
<!DOCTYPE html>
<html lang="en">
<head>
<meta charset="utf-8">
<title>Quimby's Yard & Garden Center – Business Card</title>
<link rel="stylesheet" href="https://fonts.googleapis.com/css2?family=Open+Sans:wght@400;600;700&display=swap">
<style>
  :root {
    --forest: #2c5228;
    --paper: #ffffff;
    --ink: #2b2b2b;
    --backdrop: #e9e7e2;
  }
  * { margin: 0; padding: 0; box-sizing: border-box; }
  html, body { width: 1200px; height: 900px; overflow: hidden; }
  body {
    background: var(--backdrop);
    font-family: "Open Sans", sans-serif;
    position: relative;
  }
  .card {
    position: absolute;
    left: 250px;
    width: 700px;
    height: 400px;
    box-shadow: 0 6px 18px rgba(0,0,0,0.18);
  }
  .card--front { top: 40px; background: var(--paper); }
  .card--back { top: 470px; background: var(--forest); display: flex; align-items: center; justify-content: center; }

  .brand {
    position: absolute;
    left: 60px;
    top: 82px;
    display: flex;
    align-items: center;
    gap: 14px;
  }
  .brand__mark { width: 22px; height: 22px; background: var(--forest); }
  .brand__name { font-size: 50px; font-weight: 700; color: var(--forest); line-height: 1; }

  .tagline {
    position: absolute;
    left: 84px;
    top: 178px;
    font-size: 20px;
    font-weight: 600;
    color: var(--forest);
  }

  .person {
    position: absolute;
    right: 56px;
    top: 44px;
    text-align: right;
  }
  .person__name { font-size: 28px; font-weight: 600; color: var(--forest); line-height: 1.1; }
  .person__title {
    font-size: 13px;
    letter-spacing: 6px;
    color: var(--forest);
    margin-top: 2px;
  }
  .person__rule {
    position: absolute;
    right: 64px;
    top: 100px;
    width: 150px;
    height: 2px;
    background: var(--forest);
  }

  .divider { position: absolute; height: 3px; background: var(--forest); }
  .divider--upper { left: 300px; right: 50px; top: 158px; }
  .divider--lower { left: 50px; width: 330px; top: 245px; }

  .services {
    position: absolute;
    right: 50px;
    top: 176px;
    list-style: none;
    text-align: right;
    font-size: 14px;
    font-weight: 600;
    color: var(--forest);
    line-height: 26px;
  }

  .contacts {
    position: absolute;
    left: 60px;
    top: 266px;
    list-style: none;
  }
  .contacts__item {
    display: flex;
    align-items: center;
    gap: 18px;
    height: 40px;
    font-size: 16px;
    font-weight: 600;
    color: var(--ink);
  }
  .contacts__icon {
    width: 30px; height: 30px;
    background: var(--forest);
    display: flex; align-items: center; justify-content: center;
  }
  .contacts__icon svg { width: 18px; height: 18px; }

  .back-brand {
    display: flex;
    align-items: center;
    gap: 16px;
  }
  .back-brand__mark { width: 26px; height: 26px; background: var(--paper); }
  .back-brand__name { font-size: 64px; font-weight: 700; color: var(--paper); line-height: 1; }
</style>
</head>
<body>

<section class="card card--front" aria-label="Business card front">
  <div class="brand">
    <span class="brand__mark"></span>
    <span class="brand__name">Quimby's</span>
  </div>
  <p class="tagline">Rooted in Your Yard...</p>

  <div class="person">
    <p class="person__name">Morris Quimby</p>
    <p class="person__title">Owner</p>
  </div>
  <span class="person__rule"></span>

  <span class="divider divider--upper"></span>
  <ul class="services">
    <li>- Landscaping</li>
    <li>- Lawn Maintenance</li>
    <li>- Snow Removal</li>
    <li>- Garden Center</li>
  </ul>

  <span class="divider divider--lower"></span>
  <ul class="contacts">
    <li class="contacts__item">
      <span class="contacts__icon">
        <svg viewBox="0 0 24 24" fill="none" stroke="#fff" stroke-width="1.6" stroke-linejoin="round"><path d="M5 3h4l2 5-2.5 1.5a11 11 0 0 0 6 6L16 13l5 2v4a2 2 0 0 1-2 2A16 16 0 0 1 3 5a2 2 0 0 1 2-2z"/></svg>
      </span>
      (555) 201-7784
    </li>
    <li class="contacts__item">
      <span class="contacts__icon">
        <svg viewBox="0 0 24 24" fill="none" stroke="#fff" stroke-width="1.6"><rect x="6" y="2.5" width="12" height="19" rx="2"/><line x1="10.5" y1="18.5" x2="13.5" y2="18.5"/></svg>
      </span>
      (555) 318-6092
    </li>
    <li class="contacts__item">
      <span class="contacts__icon">
        <svg viewBox="0 0 24 24" fill="none" stroke="#fff" stroke-width="1.6"><path d="M12 22s7-7 7-12a7 7 0 0 0-14 0c0 5 7 12 7 12z"/><circle cx="12" cy="10" r="2.5"/></svg>
      </span>
      482 Orchard Lane, Springfield
    </li>
  </ul>
</section>

<section class="card card--back" aria-label="Business card back">
  <div class="back-brand">
    <span class="back-brand__mark"></span>
    <span class="back-brand__name">Quimby's</span>
  </div>
</section>

</body>
</html>
```